Want a package created for a new protein bar

We would like a new package created for a new protein bar project The name of the bar will be VORNBar a real food protein bar, we would like a ‘window’ on the package of bar like Brisk Mell bar below in images.

VORNBar
‘Super Food Bar’
14g of Whey Protein
The package film size is the following 12cm width x 15cm Length,
Flavor Peanut Chocolate Chip, additional information will be attached shortly like nutrition facts,

Target Market(s)

fitness market, bodybuilders, athletes, everyday people

Industry/Entity Type

Health Product

Logo Text

VORNBar

Font styles to use
Serif
Sans Serif
Decorative

Requirements
Must have
• Package window

```html
<!DOCTYPE html>
<html lang="en">
<head>
<meta charset="utf-8">
<title>VORNBar Wrapper</title>
<link href="https://fonts.googleapis.com/css2?family=Oswald:wght@400;500;600;700&display=swap" rel="stylesheet">
<style>
  :root {
    --bg: #d4d4d4;
    --orange: #e0691f;
    --orange-dark: #c95a16;
    --orange-light: #ea7a30;
    --paper: #f1efea;
    --brown: #4a2c17;
    --white: #ffffff;
    --choc-dark: #2a130b;
    --choc-mid: #4d2516;
  }
  html, body {
    margin: 0;
    width: 1200px;
    height: 857px;
    overflow: hidden;
    background: var(--bg);
    font-family: "Oswald", "Arial Narrow", sans-serif;
  }
  .canvas { position: relative; width: 1200px; height: 857px; }
  .wrapper {
    position: absolute;
    left: 174px; top: 366px;
    width: 848px; height: 250px;
    background: var(--orange);
  }
  .crimp {
    position: absolute; top: 0; height: 100%;
    background: repeating-linear-gradient(90deg, var(--orange) 0 5px, var(--orange-dark) 5px 7px, var(--orange-light) 7px 9px);
  }
  .crimp--left { left: 0; width: 96px; }
  .crimp--right { right: 0; width: 60px; }
  .new-badge { position: absolute; left: 0; top: 0; width: 96px; height: 250px; }
  .window {
    position: absolute; left: 98px; top: 0;
    width: 180px; height: 250px;
    background: var(--white);
  }
  .window__bar {
    position: absolute; left: 24px; top: 50px;
    width: 156px; height: 168px;
    border-radius: 14px 0 0 18px;
    background: linear-gradient(160deg, var(--choc-mid), var(--choc-dark));
  }
  .brand {
    position: absolute; left: 304px; top: 36px;
    display: flex; align-items: center; gap: 10px;
    margin: 0; color: var(--white);
    font-weight: 500; font-size: 34px; line-height: 1; letter-spacing: 0;
  }
  .brand__mark {
    width: 14px; height: 14px;
    background: var(--white);
  }
  .band {
    position: absolute; left: 278px; top: 88px;
    width: 510px; height: 106px;
    background: var(--paper);
  }
  .band__title {
    position: absolute; left: 26px; top: 10px; margin: 0;
    color: var(--brown); font-weight: 700; font-size: 52px; line-height: 1; letter-spacing: 1px;
  }
  .band__sub {
    position: absolute; left: 26px; top: 70px; margin: 0;
    color: var(--brown); font-weight: 600; font-size: 27px; line-height: 1;
  }
  .product-photo {
    position: absolute; left: 694px; top: 34px;
    width: 120px; height: 168px;
    border-radius: 10px;
    background: linear-gradient(170deg, #8a4e32, #5b3020 55%, #c98b4a);
  }
  .flavor {
    position: absolute; left: 304px; top: 204px; margin: 0;
    color: var(--white); font-weight: 500; font-size: 13.5px; line-height: 1; letter-spacing: 0.4px;
  }
  .protein-amount {
    position: absolute; left: 722px; top: 214px; margin: 0;
    color: var(--white); font-weight: 600; font-size: 28px; line-height: 1; letter-spacing: 1px;
  }
</style>
</head>
<body>
<div class="canvas">
  <div class="wrapper">
    <div class="crimp crimp--left"></div>
    <svg class="new-badge" viewBox="0 0 96 250" aria-label="New">
      <polygon points="0,58 96,20 96,64 0,102" fill="#ffffff"/>
      <text x="48" y="70" text-anchor="middle" transform="rotate(-22 48 62)" font-family="Oswald, sans-serif" font-weight="700" font-size="28" fill="#4a2c17">NEW</text>
    </svg>
    <div class="window">
      <div class="window__bar" role="img" aria-label="Chocolate-coated protein bar seen through the window"></div>
    </div>
    <div class="crimp crimp--right"></div>
    <h1 class="brand"><span class="brand__mark"></span>VORNBar</h1>
    <div class="band">
      <h2 class="band__title">WHEY PROTEIN</h2>
      <p class="band__sub">SUPER FOOD BAR</p>
    </div>
    <div class="product-photo" role="img" aria-label="Photo of two halves of a chocolate peanut protein bar"></div>
    <p class="flavor">PEANUT CHOCOLATE CHIP FLAVOR</p>
    <p class="protein-amount">14 G</p>
  </div>
</div>
</body>
</html>
```